Counseling Practice Business Card

I need a professional looking business card incorporating my new logo that was just completed. Card needs to incorporate my name and title, description of my specialty, my address, my phone number, my fax number, my email and my website URL. I need to be able to choose design on/with different paper colors and textures.
I do not have a lot of business card ideas so I am open to anything but I want bold,sharp, clear card without additional designs other than my logo (see attached file info). I am open to different color backgrounds or paper colors including black. I do not like traditional brackets around area codes in phone number or dashes between numbers in phone number. Am open to other ways of presenting including periods between numbers as appropriate. I do not know enough to know what I like yet but I want card to coordinate and work together with my logo. My practice emphasizes natural mental health interventions so any use of color (with background paper color or the blue and green in my logo) that elicits nature is nice. In addition to black, any natural brown or wood looking background might be desirable also. Most of the offerings so far look very similar and boring.

Target Market(s)

Potential therapy clients and other professionals

Contact Information for Business Card

Card information:
Marcus T. Whitfield, Ph.D.
Licensed Clinical Psychologist
Integrative Health Coach
4812 Ferndale Pkwy NW
Suite 730
Duluth, GA 30096
(770) 555-0142 phone
(770) 555-0186 fax
drmarcuswhitfield@kelvora.com
pathbloomcounseling.com

Font styles to use
Serif
Sans Serif
Other font styles liked:
• anything that you think looks crisp, clear and easily readable

Requirements
Must have
• Any color used should coordinate with my logo design (see attached files).
• Card should be printed horizontally so top and bottom are longest sides of rectangle.
• Background color or paper color should complement and highlight logo. Do not like a white background. black, grey, brown or any color my logo would blend well with.
Nice to have
• I would like designer to utilize color to highlight letters/name or phone-fax-web symbols.
• Bottom edge of card could be highlighted if appropriate to an idea.
Should not have
• I would NOT want the card to have a pure white background at all.
• No clear cards.
• Cards should be oriented with long sides on bottom and top, NOT sides. DO NOT LIKE THIS THIN TALL ORIENTATION.

```html
<!DOCTYPE html>
<html lang="en">
<head>
<meta charset="utf-8">
<title>Pathbloom Counseling – Business Card</title>
<link rel="stylesheet" href="https://fonts.googleapis.com/css2?family=Source+Sans+3:wght@400;600&display=swap">
<style>
  :root{
    --page:#ffffff;
    --wood-dark:#4e3d2c;
    --wood-mid:#5c4a37;
    --wood-light:#a49682;
    --wood-light-2:#8e806d;
    --ink-white:#f4f1ec;
    --ink-blue:#2f7fc1;
  }
  html,body{margin:0;width:1200px;height:1200px;overflow:hidden;background:var(--page);}
  body{position:relative;font-family:"Source Sans 3",sans-serif;}
  .card{
    position:absolute;left:225px;top:385px;width:750px;height:429px;
    box-shadow:2px 3px 5px rgba(0,0,0,.35);overflow:hidden;
  }
  .card__wood{
    position:absolute;inset:0;
    background:linear-gradient(180deg,var(--wood-mid) 0%,var(--wood-dark) 45%,var(--wood-mid) 100%);
  }
  .card__edge{
    position:absolute;left:0;right:0;bottom:0;height:38px;
    background:linear-gradient(180deg,var(--wood-light-2),var(--wood-light) 40%,var(--wood-light-2));
  }
  .block{position:absolute;right:30px;text-align:right;white-space:nowrap;}
  .name{top:36px;font-size:32px;color:var(--ink-white);font-weight:400;letter-spacing:-.2px;line-height:1;}
  .titles{top:80px;font-size:19px;line-height:26px;color:var(--ink-blue);text-transform:uppercase;letter-spacing:-.3px;}
  .contact{position:absolute;right:68px;font-size:19px;color:var(--ink-blue);text-align:right;line-height:25px;letter-spacing:-.2px;white-space:nowrap;}
  .icon{position:absolute;right:30px;width:24px;height:24px;}
  .icon svg{width:100%;height:100%;display:block;}
  .brand{
    position:absolute;left:40px;top:322px;font-size:27px;font-weight:600;line-height:32px;
    color:var(--ink-blue);letter-spacing:.2px;white-space:nowrap;
  }
</style>
</head>
<body>
<div class="card">
  <div class="card__wood" role="img" aria-label="Dark brown wood grain texture"></div>
  <div class="card__edge" role="img" aria-label="Light wood grain strip along bottom edge"></div>

  <div class="block name">Marcus T. Whitfield, Ph.D.</div>
  <div class="block titles">Licensed Clinical Psychologist<br>Integrative Health Coach</div>

  <div class="contact" style="top:160px">4812 Ferndale Pkwy NW Suite 730<br>Duluth, GA 30096</div>
  <div class="icon" style="top:169px">
    <svg viewBox="0 0 24 24"><path d="M12 2a7 7 0 0 0-7 7c0 5 7 13 7 13s7-8 7-13a7 7 0 0 0-7-7z" fill="none" stroke="var(--ink-white)" stroke-width="2.4"/><circle cx="12" cy="9" r="2.3" fill="var(--ink-white)"/></svg>
  </div>

  <div class="contact" style="top:215px">770.555.0142</div>
  <div class="icon" style="top:215px">
    <svg viewBox="0 0 24 24"><path d="M6 3l3 4-2 2c1 3 4 6 7 7l2-2 4 3-2 3c-7 0-14-7-14-14z" fill="var(--ink-white)"/></svg>
  </div>

  <div class="contact" style="top:246px">770.555.0186</div>
  <div class="icon" style="top:246px">
    <svg viewBox="0 0 24 24"><rect x="5" y="2" width="14" height="8" fill="none" stroke="var(--ink-white)" stroke-width="1.6"/><rect x="1" y="11" width="22" height="11" fill="var(--ink-white)"/></svg>
  </div>

  <div class="contact" style="top:277px">drmarcuswhitfield@kelvora.com</div>
  <div class="icon" style="top:277px">
    <svg viewBox="0 0 24 24"><rect x="2" y="5" width="20" height="15" fill="var(--ink-white)"/><path d="M2 5l10 8 10-8" fill="none" stroke="var(--wood-dark)" stroke-width="1.5"/></svg>
  </div>

  <div class="contact" style="top:326px">pathbloomcounseling.com</div>
  <div class="icon" style="top:326px">
    <svg viewBox="0 0 24 24" fill="none" stroke="var(--ink-white)" stroke-width="1.6"><circle cx="12" cy="12" r="10"/><ellipse cx="12" cy="12" rx="4.5" ry="10"/><path d="M2 12h20M4 7h16M4 17h16"/></svg>
  </div>

  <div class="brand">Pathbloom Counseling</div>
</div>
</body>
</html>
```